QTR Business Card

Harborline Capital Partners is a successful and reputable financial services company.Our main services are home loans, commercial loans, vehicle finance and equipment finance. We also do development finance for property developers. Our company is always evolving to always be an industry leader in best financial service practices with access to the largest range of lenders in the country.

We want the business card to reflect our national finance company. Modern, professional corporate image. At the same time the concept of Harborline Capital Partners is that we help build wealth for you but the process for the client is an enjoyable peaceful experience. Not stressful at all .....

Colors to be same as the logo .... gold silver black white as the options

On the reverse side of the card I wanted either just the logo symbol or the logo symbol and text of the logo ....

It could be on a black background ..... or silver or gold .... want it to be quite striking to look at when you first see the card.

On the other side of the card I wanted the following details:

Doran Pelham
Director

0498 372 604

doran@hbcpx.com.au

Po Box 852
Tarrow ACT 2694

www.hbcpx.com.au

ACN 918 264 057 (This can be in very small print and can be in the bottom corner of the card or somewhere not very prominent)
Updates

As requested Ive uploaded the logo file in both .ai and .pdf formats. Please let me know if you need anything else. Thanks

Reason: Still deciding on which design I like best. I will provide individual feedback as well.

```html
<!DOCTYPE html>
<html lang="en">
<head>
<meta charset="utf-8">
<title>Harborline Capital Partners – Business Card</title>
<link rel="stylesheet" href="https://fonts.googleapis.com/css2?family=Cinzel:wght@500&family=Syncopate:wght@700&family=Montserrat:wght@300;400&display=swap">
<style>
  :root {
    --page: #e6e6e4;
    --paper: #fbfbfa;
    --silver-light: #f3f3f1;
    --silver: #dcdcda;
    --ink-grey: #7c7c7c;
    --gold-light: #f1e6c8;
    --gold: #dcb04c;
    --gold-deep: #cc9a2c;
    --gold-text: #c99a2e;
    --on-gold: #fffaf0;
  }
  * { box-sizing: border-box; margin: 0; padding: 0; }
  html, body { width: 1200px; height: 1200px; overflow: hidden; background: var(--page); }
  .canvas { position: relative; width: 1200px; height: 1200px; }

  .card {
    position: absolute;
    left: 150px;
    width: 900px;
    height: 514px;
    overflow: hidden;
    box-shadow: 0 10px 30px rgba(0,0,0,0.15);
  }
  .card--front { top: 56px; background: linear-gradient(180deg, var(--paper) 0%, var(--silver-light) 100%); }
  .card--back { top: 630px; background: linear-gradient(180deg, var(--silver-light) 0%, var(--gold-light) 30%, var(--gold) 75%, var(--gold-deep) 100%); }

  /* Front */
  .brand { position: absolute; left: 52px; top: 38px; display: flex; align-items: center; gap: 14px; }
  .brand__dot { width: 44px; height: 44px; border-radius: 50%; background: var(--gold); }
  .brand__name { font-family: "Cinzel", serif; font-weight: 500; font-size: 27px; color: var(--gold-text); letter-spacing: 0.02em; white-space: nowrap; }

  .holder { position: absolute; left: 62px; top: 112px; }
  .holder__name { font-family: "Syncopate", sans-serif; font-weight: 700; font-size: 40px; color: var(--ink-grey); letter-spacing: 0.02em; line-height: 1; white-space: nowrap; text-shadow: 0 1px 0 #fff, 0 2px 3px rgba(0,0,0,0.18); }
  .holder__role { margin-top: 16px; font-family: "Montserrat", sans-serif; font-weight: 400; font-size: 22px; color: var(--ink-grey); letter-spacing: 1.05em; text-transform: uppercase; }

  .band { position: absolute; left: 0; top: 232px; width: 900px; height: 282px; background: linear-gradient(180deg, var(--gold-light) 0%, var(--gold) 45%, var(--gold-deep) 100%); }

  .contact { position: absolute; display: flex; align-items: flex-start; gap: 22px; font-family: "Montserrat", sans-serif; font-weight: 300; font-size: 17px; line-height: 1.45; color: var(--on-gold); white-space: nowrap; }
  .contact svg { width: 30px; height: 30px; flex: none; }
  .contact--phone { left: 62px; top: 262px; }
  .contact--email { left: 62px; top: 322px; }
  .contact--post { left: 510px; top: 262px; }
  .contact--web { left: 510px; top: 352px; }
  .contact span { padding-top: 4px; }

  .acn { position: absolute; right: 34px; bottom: 26px; font-family: "Montserrat", sans-serif; font-weight: 400; font-size: 11px; color: var(--on-gold); }

  /* Back */
  .emblem { position: absolute; left: 50%; top: 92px; transform: translateX(-50%); display: flex; flex-direction: column; align-items: center; gap: 26px; }
  .emblem__disc { width: 200px; height: 200px; border-radius: 50%; background: var(--silver); }
  .emblem__name { font-family: "Cinzel", serif; font-weight: 500; font-size: 26px; color: var(--on-gold); letter-spacing: 0.04em; white-space: nowrap; }
</style>
</head>
<body>
<main class="canvas">

  <section class="card card--front" aria-label="Card front">
    <div class="brand">
      <div class="brand__dot"></div>
      <div class="brand__name">Harborline Capital Partners</div>
    </div>

    <div class="holder">
      <div class="holder__name">DORAN PELHAM</div>
      <div class="holder__role">Director</div>
    </div>

    <div class="band"></div>

    <div class="contact contact--phone">
      <svg viewBox="0 0 24 24" aria-hidden="true"><path fill="#fffaf0" d="M6.6 10.8a15 15 0 0 0 6.6 6.6l2.2-2.2a1 1 0 0 1 1-.25 11.4 11.4 0 0 0 3.6.57 1 1 0 0 1 1 1V20a1 1 0 0 1-1 1A17 17 0 0 1 3 4a1 1 0 0 1 1-1h3.5a1 1 0 0 1 1 1c0 1.25.2 2.45.57 3.57a1 1 0 0 1-.25 1z"/></svg>
      <span>0498 372 604</span>
    </div>
    <div class="contact contact--email">
      <svg viewBox="0 0 24 24" aria-hidden="true"><rect x="2" y="5" width="20" height="14" fill="#fffaf0"/><path d="M2 5l10 8 10-8" fill="none" stroke="#d8aa44" stroke-width="1.5"/></svg>
      <span>doran@hbcpx.com.au</span>
    </div>
    <div class="contact contact--post">
      <svg viewBox="0 0 24 24" aria-hidden="true"><path fill="#fffaf0" d="M12 2a7 7 0 0 0-7 7c0 5.2 7 13 7 13s7-7.8 7-13a7 7 0 0 0-7-7zm0 9.5A2.5 2.5 0 1 1 12 6.5a2.5 2.5 0 0 1 0 5z"/></svg>
      <span>Po Box 852<br>Tarrow ACT 2694</span>
    </div>
    <div class="contact contact--web">
      <svg viewBox="0 0 24 24" aria-hidden="true"><g fill="none" stroke="#fffaf0" stroke-width="1.6"><circle cx="12" cy="12" r="9"/><ellipse cx="12" cy="12" rx="4" ry="9"/><path d="M3 12h18M5 7h14M5 17h14"/></g></svg>
      <span>www.hbcpx.com.au</span>
    </div>

    <div class="acn">ACN 918 264 057</div>
  </section>

  <section class="card card--back" aria-label="Card back">
    <div class="emblem">
      <div class="emblem__disc"></div>
      <div class="emblem__name">Harborline Capital Partners</div>
    </div>
  </section>

</main>
</body>
</html>
```